依頼詳細
各デザインサイズ:1100㎜×450㎜
背景色:白色
フォント、矢印:アートな雰囲気(動きがあるお洒落な雰囲気)
フォント色:黒
フォントサイズ:規格内で目いっぱいの大きさ

内容:添付データの通り
※ホテル名は1列ではなく複数列でも可
※矢印の向きは変えずに形のみ変更可
※車マークはデザインに合うように変更

データ種類:①②③
各データ内は、ベースができましたら基本的に矢印の向きだけ変える形となります。
※ご提案時には、上記3種類のデータ添付をお願いいたします。

ベース案として、データを添付いたします。
参考にご利用ください。

何卒ご提案ご協力の程よろしくお願いいたします。
記載項目
ホテル名、矢印、車マーク、30秒
希望イメージ
シンプル 複雑
単色 カラフル
暗い 明るい
日常 高級
遊び心 厳粛
未来的 伝統的
女性的 男性的
希望する色
無彩色系
納品ファイル
• 高解像度JPG (.jpg)
• イラストレーター形式 (.ai)
補足説明

フォントやサイズ感が良く、実際に電柱に照らし合わせた中でイメージがGoodでした。

お忙しい中、複数のご提案を頂きありがとうございました。
今後も定期的に依頼を上げていく予定ですので、機会がございましたらご助力をお願いいたします。

```html
<!DOCTYPE html>
<html lang="ja">
<head>
<meta charset="UTF-8">
<title>MEADOW HOTEL 誘導看板</title>
<link rel="stylesheet" href="https://fonts.googleapis.com/css2?family=Anton&family=Noto+Sans+JP:wght@900&display=swap">
<style>
  :root {
    --sign-bg: #ffffff;
    --ink: #000000;
    --reverse: #ffffff;
  }
  html, body {
    margin: 0;
    padding: 0;
    overflow: hidden;
    background: var(--sign-bg);
  }
  .sign {
    position: relative;
    width: 1200px;
    height: 2904px;
    background: var(--sign-bg);
    overflow: hidden;
  }
  .hotel-name {
    position: absolute;
    top: 226px;
    left: 0;
    width: 100%;
    margin: 0;
    text-align: center;
    font-family: "Anton", "Noto Sans JP", sans-serif;
    font-weight: 400;
    font-size: 320px;
    line-height: 359px;
    letter-spacing: -4px;
    color: var(--ink);
    transform: scaleX(0.93);
    transform-origin: center top;
    white-space: nowrap;
  }
  .hotel-name span { display: block; }
  .direction-arrow {
    position: absolute;
    inset: 0;
    width: 1200px;
    height: 2904px;
  }
  .arrow-body { fill: var(--ink); }
  .car-body { fill: var(--reverse); }
  .car-glass { fill: var(--ink); }
  .travel-time {
    position: absolute;
    top: 2500px;
    left: 0;
    width: 100%;
    margin: 0;
    text-align: center;
    color: var(--reverse);
    font-size: 270px;
    line-height: 1;
    white-space: nowrap;
  }
  .travel-time .digits {
    font-family: "Anton", sans-serif;
  }
  .travel-time .unit {
    font-family: "Noto Sans JP", sans-serif;
    font-weight: 900;
    font-size: 230px;
    margin-left: 10px;
  }
</style>
</head>
<body>
  <main class="sign">
    <h1 class="hotel-name"><span>MEADOW</span><span>HOTEL</span></h1>

    <svg class="direction-arrow" viewBox="0 0 1200 2904" aria-hidden="true">
      <polygon class="arrow-body"
        points="600,1039 988,1274 737,1274 1011,2904 196,2904 470,1274 196,1274"/>
      <g class="car-icon">
        <rect class="car-body" x="512" y="2100" width="176" height="320" rx="60" ry="60"/>
        <rect class="car-body" x="492" y="2200" width="30" height="20" rx="8"/>
        <rect class="car-body" x="678" y="2200" width="30" height="20" rx="8"/>
        <path class="car-glass" d="M532,2215 Q600,2180 668,2215 L656,2270 Q600,2255 544,2270 Z"/>
        <path class="car-glass" d="M540,2360 Q600,2372 660,2360 L666,2392 Q600,2410 534,2392 Z"/>
        <rect class="car-glass" x="528" y="2280" width="10" height="70" rx="4"/>
        <rect class="car-glass" x="662" y="2280" width="10" height="70" rx="4"/>
      </g>
    </svg>

    <p class="travel-time"><span class="digits">30</span><span class="unit">秒</span></p>
  </main>
</body>
</html>
```